Trade Show Marlow 3x3 booth schel scheme

We would like to have full coverage design for 3x3 booth scheel

2x2 pop up Counter (1200mm wide x 900mm high x 400mm deep)
Our company provides food safety training, consultancy and food safety app service for hospitality businesses.

```html
<!DOCTYPE html>
<html lang="en">
<head>
<meta charset="utf-8">
<title>Calder – Pop-up Counter Wrap</title>
<link href="https://fonts.googleapis.com/css2?family=Montserrat:wght@400;600&family=Nunito:wght@800&display=swap" rel="stylesheet">
<style>
  :root {
    --lime: #c8d42e;
    --ink: #111111;
    --paper: #ffffff;
    --backdrop-light: #c9c9c9;
    --backdrop-dark: #a9a9a9;
    --guide: #666666;
    --measure: #ffffff;
  }
  html, body {
    margin: 0;
    padding: 0;
    width: 842px;
    height: 1200px;
    overflow: hidden;
  }
  body {
    background: radial-gradient(ellipse at 50% 40%, var(--backdrop-light), var(--backdrop-dark));
    position: relative;
    font-family: "Montserrat", sans-serif;
  }
  .measure-row {
    position: absolute;
    top: 420px;
    left: 61px;
    width: 720px;
    height: 24px;
  }
  .measure-row svg { position: absolute; inset: 0; }
  .measure-label {
    position: absolute;
    top: 2px;
    font-size: 15px;
    line-height: 20px;
    color: var(--measure);
    transform: translateX(-50%);
    letter-spacing: 0.04em;
    white-space: nowrap;
  }
  .measure-height {
    position: absolute;
    left: 30px;
    top: 472px;
    width: 24px;
    height: 324px;
  }
  .measure-height svg { position: absolute; inset: 0; }
  .measure-height .measure-label {
    top: 50%;
    left: 50%;
    transform: translate(-50%, -50%) rotate(-90deg);
  }
  .counter-wrap {
    position: absolute;
    top: 472px;
    left: 61px;
    width: 720px;
    height: 324px;
    background: var(--paper);
    display: grid;
    grid-template-columns: 144px 432px 144px;
    box-shadow: 0 24px 32px -12px rgba(0,0,0,0.35);
  }
  .side-panel {
    display: flex;
    align-items: center;
    justify-content: center;
  }
  .side-panel.left { border-right: 1px dashed var(--guide); }
  .side-panel.right { border-left: 1px dashed var(--guide); }
  .brand-dot {
    width: 80px;
    height: 80px;
    border-radius: 50%;
    background: var(--lime);
    margin-top: -4px;
  }
  .front-panel {
    position: relative;
    text-align: center;
  }
  .wordmark {
    position: absolute;
    top: 30px;
    left: 0;
    right: 0;
    margin: 0;
    font-weight: 600;
    font-size: 58px;
    letter-spacing: 0.16em;
    padding-left: 0.16em;
    color: var(--ink);
    line-height: 1;
  }
  .wordmark-rule {
    position: absolute;
    top: 99px;
    left: 70px;
    width: 292px;
    height: 2px;
    background: var(--lime);
  }
  .tagline {
    position: absolute;
    top: 112px;
    left: 0;
    right: 0;
    margin: 0;
    font-weight: 400;
    font-size: 22px;
    letter-spacing: 0.19em;
    padding-left: 0.19em;
    line-height: 26px;
    color: var(--ink);
  }
  .services {
    position: absolute;
    top: 186px;
    left: 66px;
    width: 300px;
    display: grid;
    grid-template-columns: 1fr 1.15fr 1fr;
  }
  .service {
    display: flex;
    flex-direction: column;
    align-items: center;
  }
  .service + .service { border-left: 1px solid var(--ink); }
  .service-icon {
    width: 42px;
    height: 42px;
    border-radius: 50%;
    background: var(--lime);
  }
  .service-name {
    margin-top: 4px;
    font-family: "Nunito", sans-serif;
    font-weight: 800;
    font-size: 14px;
    line-height: 18px;
    color: var(--ink);
    white-space: nowrap;
  }
  .web-address {
    position: absolute;
    top: 273px;
    left: 50%;
    transform: translateX(-50%);
    width: 192px;
    height: 22px;
    line-height: 22px;
    border-radius: 11px;
    background: var(--lime);
    font-family: "Nunito", sans-serif;
    font-weight: 800;
    font-size: 12px;
    color: var(--ink);
    white-space: nowrap;
  }
</style>
</head>
<body>

  <div class="measure-row">
    <svg width="720" height="24" viewBox="0 0 720 24">
      <g stroke="var(--measure)" fill="var(--measure)" stroke-width="1">
        <line x1="0" y1="12" x2="28" y2="12"/>
        <line x1="112" y1="12" x2="144" y2="12"/>
        <line x1="144" y1="12" x2="312" y2="12"/>
        <line x1="408" y1="12" x2="576" y2="12"/>
        <line x1="576" y1="12" x2="604" y2="12"/>
        <line x1="690" y1="12" x2="720" y2="12"/>
        <polygon points="0,12 7,7 7,17"/>
        <polygon points="144,12 137,7 137,17"/>
        <polygon points="144,12 151,7 151,17"/>
        <polygon points="576,12 569,7 569,17"/>
        <polygon points="576,12 583,7 583,17"/>
        <polygon points="720,12 713,7 713,17"/>
      </g>
    </svg>
    <span class="measure-label" style="left:72px">400MM</span>
    <span class="measure-label" style="left:360px">1200MM</span>
    <span class="measure-label" style="left:648px">400MM</span>
  </div>

  <div class="measure-height">
    <svg width="24" height="324" viewBox="0 0 24 324">
      <g stroke="var(--measure)" fill="var(--measure)" stroke-width="1">
        <line x1="12" y1="0" x2="12" y2="120"/>
        <line x1="12" y1="204" x2="12" y2="324"/>
        <polygon points="12,0 7,7 17,7"/>
        <polygon points="12,324 7,317 17,317"/>
      </g>
    </svg>
    <span class="measure-label">900MM</span>
  </div>

  <main class="counter-wrap">
    <section class="side-panel left">
      <div class="brand-dot"></div>
    </section>

    <section class="front-panel">
      <h1 class="wordmark">CALDER</h1>
      <div class="wordmark-rule"></div>
      <p class="tagline">FOOD HYGIENE AND<br>HEALTH SAFETY</p>

      <div class="services">
        <div class="service">
          <div class="service-icon" role="img" aria-label="Training icon: trainer presenting at a flip chart"></div>
          <span class="service-name">Training</span>
        </div>
        <div class="service">
          <div class="service-icon" role="img" aria-label="Consultancy icon: consultant with ideas and documents"></div>
          <span class="service-name">Consultancy</span>
        </div>
        <div class="service">
          <div class="service-icon" role="img" aria-label="Safety app icon: hand tapping a smartphone"></div>
          <span class="service-name">Safety App</span>
        </div>
      </div>

      <div class="web-address">www.caldersolutions.co.uk</div>
    </section>

    <section class="side-panel right">
      <div class="brand-dot"></div>
    </section>
  </main>

</body>
</html>
```